Book cover for publishing doctoral research about various national styles of piano playing.

I need a book cover for a publication of a doctoral research with regard to styles of piano performance characteristic to various nations.

Any images or graphics are optional, typography seems most important, but please feel free to be creative.

I attach the barcode, qsr and publisher's logo in the next few days. (Logo is still being designed).

For various reasons the size of the book is not completely decided yet. Please create your design in 7" x 10", but if at all possible, I would like to ask for files of two sizes, also including 8.5" x 11" in the final submission.

I am looking for a design that looks professional, probably simple, but I am open to any suggestions.
Updates

Dear Designers,I would like to thank you all for participation and submitting so many high-quality designs.My final decision was based on the feedback I received from my professional colleagues and potential readers.I would like to wish you all the best for the future.Best wishes,Radosław Added Monday, December 21, 2015

Target Market(s)

Pianists, students, music professionals

Industry/Entity Type

Publishing

Requirements
Must have
• Title: Tracing Regional Keyboard Lineages
• Subtitle: Origins and legacies
• Author: Radosław Kępiński
• Space for my logo on the front page and the spine.
• On the back page, please include some space for a short biography, 'barcode' and 'qsr' code.
• Please include whatever else you consider necessary.
Nice to have
• Would it be possible to use the same cover to a e-book edition?

```html
<!DOCTYPE html>
<html lang="en">
<head>
<meta charset="utf-8">
<title>Tracing Regional Keyboard Lineages — Cover</title>
<link rel="stylesheet" href="https://fonts.googleapis.com/css2?family=Amatic+SC:wght@700&family=Oswald:wght@700&display=swap">
<style>
  :root {
    --cover-black: #151515;
    --ink-cream: #f1ece0;
    --keys-cream: #eee9dc;
    --keys-shade: #d9d3c4;
    --accent-yellow: #e6e23a;
  }
  html, body {
    margin: 0;
    padding: 0;
    width: 982px;
    height: 1200px;
    overflow: hidden;
    background: var(--cover-black);
  }
  .cover {
    position: relative;
    width: 982px;
    height: 1200px;
    background: radial-gradient(ellipse at 50% 55%, #1d1d1d 0%, var(--cover-black) 70%);
    overflow: hidden;
  }
  .keyboard-band {
    position: absolute;
    top: 0;
    left: 0;
    width: 982px;
    height: 240px;
    background: linear-gradient(180deg, var(--keys-cream) 0%, var(--keys-shade) 100%);
  }
  .title {
    position: absolute;
    top: 250px;
    left: 90px;
    right: 60px;
    margin: 0;
    font-family: "Amatic SC", cursive;
    font-weight: 700;
    font-size: 178px;
    line-height: 168px;
    letter-spacing: 4px;
    color: var(--ink-cream);
    text-transform: uppercase;
  }
  .title span { display: block; }
  .subtitle {
    position: absolute;
    top: 940px;
    left: 150px;
    margin: 0;
    font-family: "Amatic SC", cursive;
    font-weight: 700;
    font-size: 58px;
    letter-spacing: 2px;
    color: var(--accent-yellow);
    text-transform: uppercase;
  }
  .subtitle .joiner { color: var(--ink-cream); }
  .author {
    position: absolute;
    top: 1040px;
    left: 150px;
    margin: 0;
    font-family: "Oswald", sans-serif;
    font-weight: 700;
    font-size: 54px;
    letter-spacing: 2px;
    color: var(--accent-yellow);
    text-transform: uppercase;
  }
</style>
</head>
<body>
  <main class="cover">
    <div class="keyboard-band" role="img" aria-label="Row of piano keys, cream white keys with black keys hanging down"></div>
    <h1 class="title">
      <span>Tracing</span>
      <span>Regional</span>
      <span>Keyboard</span>
      <span>Lineages</span>
    </h1>
    <p class="subtitle">Origins <span class="joiner">and</span> legacies</p>
    <p class="author">Radosław Kępiński</p>
  </main>
</body>
</html>
```